I need someone to help me finish my logo for Tavrin Honey and create a honey label template I can use and amend for each harvest.
I created some basic labels last year but I want the quality to be better as my partner made the logo in Word. I also want a label with more detail so I can sell the honey to local shops e.g. include nutritionals, ingredients, address. Visit tavrinhoney on instagram to see more and examples of last years label in situ.

```html
<!DOCTYPE html>
<html lang="en">
<head>
<meta charset="utf-8">
<title>Tavrin Honey – Jar Label Template</title>
<link rel="stylesheet" href="https://fonts.googleapis.com/css2?family=Heebo:wght@300;400&display=swap">
<style>
  :root {
    --board: #e4e4e4;
    --label: #ffffff;
    --ink: #1a1a1a;
    --muted: #555555;
    --purple: #6a1f86;
    --purple-deep: #3b0d4e;
    --purple-soft: #c9a0cf;
    --rule: #222222;
    --line-pattern: #efefef;
  }
  * { margin: 0; padding: 0; box-sizing: border-box; }
  html, body { width: 1200px; height: 960px; overflow: hidden; }
  body {
    background: var(--board);
    font-family: "Heebo", Arial, sans-serif;
    font-weight: 300;
    color: var(--ink);
    position: relative;
  }

  /* Dimension annotations */
  .dimension { position: absolute; color: #777; font-size: 12px; }
  .dimension--height { left: 82px; width: 40px; }
  .dimension__rule-v { position: absolute; left: 19px; width: 1px; background: #555; }
  .dimension__tick-h { position: absolute; left: 0; width: 38px; height: 1px; background: #555; }
  .dimension__text { position: absolute; left: 0; width: 40px; text-align: center; background: var(--board); }
  .dimension--width { top: 460px; left: 140px; width: 978px; height: 34px; }
  .dimension__rule-h { position: absolute; top: 17px; left: 0; right: 0; height: 1px; background: #555; }
  .dimension__tick-v { position: absolute; top: 0; width: 1px; height: 34px; background: #555; }
  .dimension--width .dimension__text { top: 9px; left: 460px; width: 60px; }

  /* Label */
  .label {
    position: absolute;
    left: 140px;
    width: 978px;
    height: 283px;
    background: var(--label);
    box-shadow: 6px 8px 12px rgba(0,0,0,0.25);
    overflow: hidden;
  }
  .label--purple { top: 157px; }
  .label--line { top: 519px; }

  .mini-brand { position: absolute; left: 128px; top: 14px; width: 100px; text-align: center; }
  .mini-brand__name { font-size: 19px; letter-spacing: 0.5px; line-height: 1; }
  .mini-brand__tag { font-size: 5px; letter-spacing: 0.4px; color: var(--purple); }
  .label--line .mini-brand__tag { color: var(--ink); }

  .blurb { position: absolute; left: 49px; top: 50px; font-size: 12.5px; line-height: 15px; color: var(--muted); }
  .ingredients { position: absolute; left: 49px; top: 88px; font-size: 12.5px; line-height: 15px; }
  .ingredients__title { font-weight: 400; }
  .date { position: absolute; left: 47px; top: 132px; font-size: 12.5px; font-weight: 400; }
  .date__line { position: absolute; left: 29px; top: 15px; width: 140px; height: 1px; background: #888; }
  .address { position: absolute; left: 49px; top: 155px; font-size: 12.5px; line-height: 15.2px; }
  .address__name { font-weight: 400; }

  .social { position: absolute; left: 202px; top: 200px; display: flex; align-items: center; gap: 5px; font-size: 12.5px; font-weight: 400; color: var(--purple); }
  .social__dot { width: 16px; height: 16px; border: 1.2px solid currentColor; border-radius: 50%; }
  .label--line .social { color: var(--ink); }

  .nutrition { position: absolute; left: 321px; top: 42px; width: 177px; }
  .nutrition__title { font-size: 12px; font-weight: 400; line-height: 14px; }
  .nutrition__serving { font-size: 8.5px; line-height: 12px; border-bottom: 2.5px solid var(--rule); padding-bottom: 2px; }
  .nutrition__table { width: 100%; border-collapse: collapse; font-size: 8.8px; border-bottom: 2.5px solid var(--rule); }
  .nutrition__table td { height: 14px; padding: 0; border-bottom: 0.8px solid var(--rule); white-space: nowrap; }
  .nutrition__table tr:last-child td { border-bottom: none; }
  .nutrition__table td:nth-child(1) { width: 84px; }
  .nutrition__table td:nth-child(2) { width: 32px; text-align: right; }
  .nutrition__table td:nth-child(3) { width: 61px; text-align: right; }

  .bee-artwork {
    position: absolute; left: 624px; top: 34px; width: 188px; height: 150px;
    background: linear-gradient(135deg, #f4f4f4, #e6e6e6);
    border-radius: 4px;
  }
  .brand { position: absolute; left: 700px; top: 152px; width: 170px; text-align: center; }
  .brand__name { font-size: 35px; line-height: 40px; letter-spacing: 0.5px; color: var(--ink); }
  .brand__tag { font-size: 12.5px; line-height: 14px; letter-spacing: 0.3px; color: var(--purple); }
  .label--line .brand__tag { color: var(--ink); }

  .weight { position: absolute; left: 620px; top: 223px; font-size: 22px; color: var(--purple); }
  .label--line .weight { color: var(--ink); }

  .mountain-band {
    position: absolute; left: 0; right: 0; bottom: 0; height: 68px;
    clip-path: polygon(0% 0%, 9.4% 4%, 21.6% 76%, 28% 6%, 38.6% 70%, 53.4% 53%, 64% 94%, 76.4% 13%, 85% 14%, 100% 0%, 100% 100%, 0% 100%);
  }
  .label--purple .mountain-band { background: linear-gradient(90deg, var(--purple-deep), var(--purple) 35%, var(--purple-soft) 60%, var(--purple) 85%, var(--purple-deep)); }
  .label--line .mountain-band { background: linear-gradient(180deg, var(--line-pattern), #fafafa); }
</style>
</head>
<body>

  <div class="dimension dimension--height" style="top:157px;height:283px;">
    <span class="dimension__tick-h" style="top:0;"></span>
    <span class="dimension__rule-v" style="top:0;height:283px;"></span>
    <span class="dimension__tick-h" style="top:282px;"></span>
    <span class="dimension__text" style="top:130px;">45mm</span>
  </div>
  <div class="dimension dimension--height" style="top:519px;height:283px;">
    <span class="dimension__tick-h" style="top:0;"></span>
    <span class="dimension__rule-v" style="top:0;height:283px;"></span>
    <span class="dimension__tick-h" style="top:282px;"></span>
    <span class="dimension__text" style="top:130px;">45mm</span>
  </div>
  <div class="dimension dimension--width">
    <span class="dimension__tick-v" style="left:0;"></span>
    <span class="dimension__rule-h"></span>
    <span class="dimension__tick-v" style="right:0;"></span>
    <span class="dimension__text">155mm</span>
  </div>

  <section class="label label--purple">
    <div class="mini-brand"><div class="mini-brand__name">TAVRIN</div><div class="mini-brand__tag">PURE RAW HONEY</div></div>
    <p class="blurb">Pure, raw and unfiltered honey harvested from<br>Tavrin hives in Ashvale and Bellmount NSW.</p>
    <div class="ingredients"><div class="ingredients__title">Ingredients:</div><div>100% Australian Honey.</div></div>
    <div class="date">Date:<span class="date__line"></span></div>
    <address class="address" style="font-style:normal;"><div class="address__name">Tavrin Honey</div><div>Harwick Lane</div><div>Bellmount</div><div>NSW Australia</div></address>
    <div class="social"><span class="social__dot"></span>@tavrinhoney</div>
    <div class="nutrition">
      <div class="nutrition__title">Nutritional Information</div>
      <div class="nutrition__serving">Serving Size 1 Tbsp (20g)</div>
      <table class="nutrition__table">
        <tr><td>Content</td><td>Per Serving</td><td>Per 100g</td></tr>
        <tr><td>Energy</td><td>303kj</td><td>1514kj</td></tr>
        <tr><td>Protein</td><td>0.06g</td><td>0.3g</td></tr>
        <tr><td>Total Fat</td><td>0g</td><td>0g</td></tr>
        <tr><td>Saturated Fat</td><td>0g</td><td>0g</td></tr>
        <tr><td>Trans Fat</td><td>0g</td><td>0g</td></tr>
        <tr><td>Total Carbohydrate</td><td>17.8g</td><td>89.1g</td></tr>
        <tr><td>Sugars</td><td>17.6g</td><td>88.1g</td></tr>
        <tr><td>Sodium</td><td>3.2mg</td><td>16.2mg</td></tr>
        <tr><td>Dietary Fiber</td><td>0g</td><td>&lt;1g</td></tr>
      </table>
    </div>
    <div class="bee-artwork" role="img" aria-label="Geometric line illustration of a bee"></div>
    <div class="brand"><div class="brand__name">TAVRIN</div><div class="brand__tag">PURE RAW HONEY</div></div>
    <div class="weight">350gr</div>
    <div class="mountain-band" role="img" aria-label="Purple low-poly mountain pattern"></div>
  </section>

  <section class="label label--line">
    <div class="mini-brand"><div class="mini-brand__name">TAVRIN</div><div class="mini-brand__tag">PURE RAW HONEY</div></div>
    <p class="blurb">Pure, raw and unfiltered honey harvested from<br>Tavrin hives in Ashvale and Bellmount NSW.</p>
    <div class="ingredients"><div class="ingredients__title">Ingredients:</div><div>100% Australian Honey.</div></div>
    <div class="date">Date:<span class="date__line"></span></div>
    <address class="address" style="font-style:normal;"><div class="address__name">Tavrin Honey</div><div>Harwick Lane</div><div>Bellmount</div><div>NSW Australia</div></address>
    <div class="social"><span class="social__dot"></span>@tavrinhoney</div>
    <div class="nutrition">
      <div class="nutrition__title">Nutritional Information</div>
      <div class="nutrition__serving">Serving Size 1 Tbsp (20g)</div>
      <table class="nutrition__table">
        <tr><td>Content</td><td>Per Serving</td><td>Per 100g</td></tr>
        <tr><td>Energy</td><td>303kj</td><td>1514kj</td></tr>
        <tr><td>Protein</td><td>0.06g</td><td>0.3g</td></tr>
        <tr><td>Total Fat</td><td>0g</td><td>0g</td></tr>
        <tr><td>Saturated Fat</td><td>0g</td><td>0g</td></tr>
        <tr><td>Trans Fat</td><td>0g</td><td>0g</td></tr>
        <tr><td>Total Carbohydrate</td><td>17.8g</td><td>89.1g</td></tr>
        <tr><td>Sugars</td><td>17.6g</td><td>88.1g</td></tr>
        <tr><td>Sodium</td><td>3.2mg</td><td>16.2mg</td></tr>
        <tr><td>Dietary Fiber</td><td>0g</td><td>&lt;1g</td></tr>
      </table>
    </div>
    <div class="bee-artwork" role="img" aria-label="Geometric line illustration of a bee"></div>
    <div class="brand"><div class="brand__name">TAVRIN</div><div class="brand__tag">PURE RAW HONEY</div></div>
    <div class="weight">350gr</div>
    <div class="mountain-band" role="img" aria-label="Black line low-poly mountain pattern"></div>
  </section>

</body>
</html>
```